Strategic Plan Notecards (4.25in x 5.5 in)

I need a design for project cards that will be handed out to the general public as part of a Strategic Planning effort for a client. I'd like the cards to be 4.25 x 5.5 so that they can be printed 4 to a US letter-size sheet of paper.

The Project title is "City of Fieldhaven Strategic Plan Update"
Needs to include text:

For more info, go to www.plainsfutureplan.org
Take the Vision Survey at http://tnyurl.example/FieldhavenIdeas
What do YOU want Fieldhaven to be?

Other variations on this text will be considered.

Target Market(s)

General Public

Font styles to use
Serif
Sans Serif

Colors

Designer to choose colors to be used in the design.

Requirements
Must have
• An interesting and fun visual appeal. Nothing stuffy. Should have a bright graphic background and interesting typefaces for the text.
Nice to have
• One of the biggest assets in the community is the Missouri River - some depiction of a river would be great.

```html
<!DOCTYPE html>
<html lang="en">
<head>
<meta charset="utf-8">
<title>City of Fieldhaven – Strategic Plan Update</title>
<link href="https://fonts.googleapis.com/css2?family=Josefin+Sans:wght@300&family=Montserrat:wght@600;700;800&display=swap" rel="stylesheet">
<style>
  :root {
    --navy-panel: #3a4663;
    --navy-text: #1f3b6b;
    --yellow: #fbc24a;
    --orange: #f3a12a;
    --orange-deep: #ef962a;
    --white: #ffffff;
    --river-blue: #2f7fb0;
    --river-deep: #1d5f8f;
    --bank-green: #6f8a4a;
    --sky: #9ec3e0;
  }
  * { margin: 0; padding: 0; box-sizing: border-box; }
  html, body { width: 1054px; height: 1200px; overflow: hidden; background: var(--yellow); }
  .card { position: relative; width: 1054px; height: 1200px; overflow: hidden; }
  .card-art { position: absolute; inset: 0; }
  .text { position: absolute; white-space: nowrap; }

  .title-city {
    left: 36px; top: 48px;
    font-family: "Josefin Sans", sans-serif; font-weight: 300;
    color: var(--yellow); font-size: 100px; line-height: 1; letter-spacing: 1px;
  }
  .title-city .small-caps { font-size: 74px; }
  .title-city .word-of { font-size: 70px; margin-left: 16px; }
  .title-name {
    left: 160px; top: 204px;
    font-family: "Josefin Sans", sans-serif; font-weight: 300;
    color: var(--yellow); font-size: 84px; line-height: 1; letter-spacing: 1px;
  }
  .title-name .small-caps { font-size: 64px; }
  .title-sub {
    left: 162px; top: 296px;
    font-family: "Montserrat", sans-serif; font-weight: 700;
    color: var(--white); font-size: 46px; line-height: 67px;
  }

  .rule { position: absolute; width: 3px; }
  .rule-title { left: 132px; top: 243px; height: 209px; background: var(--white); }
  .rule-body { left: 132px; top: 565px; height: 635px; background: var(--navy-text); }

  .question {
    left: 162px; top: 648px;
    font-family: "Montserrat", sans-serif; font-weight: 700;
    color: var(--navy-text); font-size: 56px; line-height: 76px;
  }
  .survey {
    left: 162px; top: 832px;
    font-family: "Montserrat", sans-serif; font-weight: 700;
    color: var(--navy-text); font-size: 34px; line-height: 55px;
  }

  .info-pill {
    position: absolute; left: 133px; top: 987px; width: 855px; height: 148px;
    background: var(--navy-panel); border-radius: 0 74px 74px 0;
    padding: 22px 0 0 29px;
    font-family: "Montserrat", sans-serif; color: var(--white);
  }
  .info-pill .lead { font-size: 40px; font-weight: 600; line-height: 52px; }
  .info-pill .site { font-size: 36px; font-weight: 800; line-height: 58px; letter-spacing: 0.3px; }
</style>
</head>
<body>
<main class="card">
  <svg class="card-art" width="1054" height="1200" viewBox="0 0 1054 1200" aria-hidden="false">
    <defs>
      <linearGradient id="aerialRiver" x1="0" y1="0" x2="1" y2="0.4">
        <stop offset="0" stop-color="var(--bank-green)"/>
        <stop offset="0.55" stop-color="var(--river-blue)"/>
        <stop offset="1" stop-color="var(--river-deep)"/>
      </linearGradient>
      <linearGradient id="bridgeReflection" x1="0" y1="0" x2="0" y2="1">
        <stop offset="0" stop-color="var(--sky)"/>
        <stop offset="0.5" stop-color="#b7a17a"/>
        <stop offset="1" stop-color="#5d84a6"/>
      </linearGradient>
    </defs>

    <rect class="aerial-photo" x="0" y="0" width="1054" height="490" fill="url(#aerialRiver)"
          role="img" aria-label="Aerial photo of the river with road and railroad bridges crossing it"/>

    <path class="yellow-field" d="M0 470 C 300 455, 700 430, 1054 408 L1054 1200 L0 1200 Z" fill="var(--yellow)"/>
    <path class="wave-band" d="M690 444 C 820 436, 940 424, 1054 414" fill="none" stroke="var(--navy-panel)" stroke-width="9"/>

    <circle class="title-panel" cx="305" cy="250" r="320" fill="var(--navy-panel)" fill-opacity="0.96"/>

    <circle class="blob-left" cx="30" cy="524" r="52" fill="var(--orange)"/>
    <circle class="blob-right" cx="955" cy="1000" r="122" fill="var(--orange)"/>
    <rect class="blob-right-body" x="955" y="1000" width="99" height="200" fill="var(--orange)"/>
    <circle class="blob-corner" cx="905" cy="1225" r="120" fill="var(--orange-deep)"/>

    <circle class="bridge-photo" cx="836" cy="486" r="140" fill="url(#bridgeReflection)"
            stroke="var(--yellow)" stroke-width="9"
            role="img" aria-label="Photo of a steel truss railroad bridge reflected in calm river water"/>
  </svg>

  <div class="text title-city">C<span class="small-caps">ITY</span><span class="word-of small-caps">OF</span></div>
  <div class="text title-name">F<span class="small-caps">IELDHAVEN</span></div>
  <span class="rule rule-title"></span>
  <div class="text title-sub">Strategic<br>Plan Update</div>

  <span class="rule rule-body"></span>
  <h1 class="text question" style="font-weight:700">What do YOU want<br>FIELDHAVEN to be?</h1>
  <p class="text survey">Take the Vision Survey at<br>http://tnyurl.example/FieldhavenIdeas</p>

  <div class="info-pill">
    <p class="lead">For more info, go to</p>
    <p class="site">WWW.PLAINSFUTUREPLAN.ORG</p>
  </div>
</main>
</body>
</html>
```